Business Card Design - Carrington Hill Lodge

We are looking at a new design for our business cards that has a modern and professional look. We run a residential aged care facility focussing on the care of residents. The cards will be used for potential clients, consultants and business opportunities in this sector. Blue and white is our main colours and would to see these colours incorporated in the design.
Industry/Entity Type
Business
Contact Information for Business Card
Carrington Hill Lodge, Darren Pelham, dpelham@carringtonhilllodge.com.au, Finance Manager, 0491 736 208, BCom, 48 Yarrabee Way, Marlow Heights, QLD 4063.

```html
<!DOCTYPE html>
<html lang="en">
<head>
<meta charset="utf-8">
<title>Carrington Hill Lodge – Business Card</title>
<link rel="stylesheet" href="https://fonts.googleapis.com/css2?family=Open+Sans:ital,wght@0,300;0,400;0,600;1,400&display=swap">
<style>
  :root {
    --page: #ece9e5;
    --card-white: #ffffff;
    --band-grey: #cdc7c2;
    --ink-grey: #5d5a58;
    --teal: #5a9db3;
    --teal-dark: #3d6f87;
    --teal-light: #80b8cc;
    --title-ink: #2f556a;
    --tagline-ink: #f3f8fa;
    --icon-bg: #9aa8ae;
  }
  * { box-sizing: border-box; margin: 0; padding: 0; }
  html, body { width: 1200px; height: 1023px; overflow: hidden; }
  body {
    background: var(--page);
    font-family: "Open Sans", Arial, sans-serif;
    position: relative;
  }
  .card {
    position: absolute;
    left: 250px;
    width: 700px;
    height: 400px;
    border-radius: 4px;
    box-shadow: 0 6px 18px rgba(0,0,0,0.18);
    overflow: hidden;
  }
  /* Front */
  .card-front { top: 60px; background: var(--card-white); }
  .band {
    position: absolute; left: 0; top: 0; width: 100%; height: 110px;
    background: var(--band-grey);
  }
  .holder { position: absolute; left: 36px; top: 36px; color: #fff; }
  .holder-name { font-size: 30px; font-weight: 400; letter-spacing: 0.5px; line-height: 1.1; }
  .holder-role { font-size: 15px; font-weight: 400; margin-top: 4px; }
  .brand {
    position: absolute; right: 30px; top: 18px;
    display: flex; align-items: center; gap: 12px;
    background: var(--card-white);
    padding: 14px 18px;
    border-radius: 4px;
  }
  .brand-dot { width: 44px; height: 44px; border-radius: 50%; background: var(--teal); flex: none; }
  .brand-name {
    font-size: 17px; font-weight: 600; letter-spacing: 1.5px;
    text-transform: uppercase; color: var(--teal); line-height: 1.2;
  }
  .address {
    position: absolute; right: 40px; top: 170px;
    text-align: right; color: var(--ink-grey);
    font-size: 16px; letter-spacing: 1px; text-transform: uppercase; line-height: 1.6;
  }
  .contact {
    position: absolute; left: 36px; bottom: 34px;
    list-style: none; color: var(--ink-grey); font-size: 15px;
  }
  .contact li { display: flex; align-items: center; gap: 10px; line-height: 1.65; }
  .contact svg { width: 16px; height: 16px; flex: none; }
  /* Back */
  .card-back {
    top: 560px;
    background: linear-gradient(135deg, var(--teal-dark) 0%, var(--teal) 55%, var(--teal-light) 100%);
  }
  .back-title {
    position: absolute; left: 44px; top: 46px;
    font-size: 36px; font-weight: 300; letter-spacing: 4px;
    text-transform: uppercase; color: var(--title-ink);
  }
  .back-tagline {
    position: absolute; left: 46px; top: 100px;
    font-size: 22px; font-style: italic; color: var(--tagline-ink); letter-spacing: 0.5px;
  }
</style>
</head>
<body>
  <section class="card card-front" aria-label="Business card front">
    <div class="band"></div>
    <div class="holder">
      <p class="holder-name">Darren Pelham</p>
      <p class="holder-role">Finance Manager</p>
    </div>
    <div class="brand">
      <span class="brand-dot"></span>
      <span class="brand-name">Carrington Hill Lodge</span>
    </div>
    <p class="address">BCom, 48 Yarrabee Way<br>Marlow Heights, QLD 4063.</p>
    <ul class="contact">
      <li>
        <svg viewBox="0 0 16 16" aria-hidden="true"><rect width="16" height="16" rx="2" fill="var(--icon-bg)"/><path d="M5 3.5l2 2-1 1.2c.6 1.4 1.6 2.4 3 3l1.2-1 2 2-1.2 1.5C7.5 12 4 8.5 3.8 4.7z" fill="#fff"/></svg>
        0491 736 208
      </li>
      <li>
        <svg viewBox="0 0 16 16" aria-hidden="true"><rect width="16" height="16" rx="2" fill="var(--icon-bg)"/><rect x="3" y="4.5" width="10" height="7" fill="none" stroke="#fff" stroke-width="1.2"/><path d="M3 4.5l5 4 5-4" fill="none" stroke="#fff" stroke-width="1.2"/></svg>
        dpelham@carringtonhilllodge.com.au
      </li>
      <li>
        <svg viewBox="0 0 16 16" aria-hidden="true"><rect width="16" height="16" rx="2" fill="var(--icon-bg)"/><circle cx="8" cy="8" r="4.5" fill="none" stroke="#fff" stroke-width="1.1"/><path d="M3.5 8h9M8 3.5c-2 2.5-2 6.5 0 9M8 3.5c2 2.5 2 6.5 0 9" fill="none" stroke="#fff" stroke-width="1"/></svg>
        www.carringtonhilllodge.com.au
      </li>
    </ul>
  </section>

  <section class="card card-back" aria-label="Business card back">
    <h1 class="back-title">Carrington Hill Lodge</h1>
    <p class="back-tagline">Comfort, Respect, Wellbeing</p>
  </section>
</body>
</html>
```